Wendell's Otter Cove-July 12th deadline-Outdoor Bait & Tackle Store needs website build, logo fine

Hi, I am buying a marina business that will serve the local community and I need a website built and our logo classed up. It is a hunting/fishing/outdoorsman store with a sexy mermaid theme. I need a fully functioning mermaid themed hunting and fishing outdoor sport and gas station website. I have purchased a domain and hosting from parvelo. WendellsOtterCove.com and @quillbox. I need to set up for live video feeds and posted video feeds into the site. and easy access to this section for me to continually add videos. Seeking a webmaster after that.

Target Market(s)

Males 21+

Coding

Coded - Design and coding required

Number of Pages Required

5+ page

Font styles to use
Script

Colors
33a6d7
6b449b
fffefe
d3a5cc
eea4c8

Requirements
Must have
• See images, I lost my upload once n snagged screen shots
Login click button over 21 +log ins with email registration for video portion
Nice to have
• Help with getting all of the live stream cameras connected

```html
<!DOCTYPE html>
<html lang="en">
<head>
<meta charset="utf-8">
<title>Wendell's Otter Cove</title>
<link href="https://fonts.googleapis.com/css2?family=Kaushan+Script&family=Montserrat:wght@400;500;600;700&display=swap" rel="stylesheet">
<style>
:root{
  --teal-sky:#a8e8e4;
  --blue:#33a6d7;
  --purple:#6b449b;
  --ink:#2e1d5e;
  --white:#fffefe;
  --mauve:#d3a5cc;
  --pink:#eea4c8;
  --sea:#2f55d8;
  --play:#e3131b;
  --button:#c98cc7;
}
*{box-sizing:border-box;margin:0;padding:0}
html,body{width:1200px;height:3720px;overflow:hidden;background:var(--white);font-family:'Montserrat',sans-serif;color:#111}
.page{position:relative;width:1200px;height:3720px;overflow:hidden}

/* hero */
.hero{position:absolute;left:0;top:0;width:1200px;height:703px;background:var(--teal-sky);overflow:hidden}
.hero-water{position:absolute;left:0;top:580px;width:1200px;height:123px}
.hero-art{position:absolute;left:430px;top:60px;width:580px;height:643px;border-radius:260px 260px 0 0;background:linear-gradient(160deg,#ef6a2a 0%,#e9d98a 35%,#3fb59a 65%,#4b4b4b 100%);opacity:.85}
.element-wheel{position:absolute;left:917px;top:-7px;width:332px;height:332px;border-radius:50%;background:radial-gradient(circle at 45% 45%,#5a9fd9 0%,#2d6fb3 70%,#1e4f8c 100%)}
.brand{position:absolute;left:144px;top:58px;font-weight:700;font-size:30px;line-height:1.1;color:var(--purple);width:230px}
.nav{position:absolute;top:26px;left:596px;display:flex;gap:8px;align-items:center}
.btn-pill{display:inline-flex;align-items:center;justify-content:center;height:46px;border-radius:23px;color:var(--white);font-weight:700;font-size:15px;letter-spacing:.3px}
.btn-login{width:122px;background:var(--blue)}
.btn-register{width:153px;background:var(--purple)}
.menu-icon{margin-left:20px;width:24px;height:20px;display:flex;flex-direction:column;justify-content:space-between}
.menu-icon span{display:block;height:4px;background:#1a1a1a;border-radius:1px}
.hero-title{position:absolute;left:141px;top:322px;font-family:'Kaushan Script',cursive;font-weight:400;font-size:66px;line-height:80px;color:var(--ink);letter-spacing:-1px;white-space:nowrap}
.hero-text{position:absolute;left:143px;top:500px;width:380px;font-size:18px;line-height:26px;font-weight:500;color:#1c1c1c}
.btn-start{position:absolute;left:144px;top:582px;width:181px;height:56px;border-radius:28px;background:var(--button);color:var(--white);font-weight:700;font-size:15px;display:flex;align-items:center;justify-content:center}
.slider-dots{position:absolute;left:1133px;top:486px;display:flex;flex-direction:column;gap:13px}
.slider-dots span{width:6px;height:6px;border-radius:50%;background:#c8c8c8}
.slider-dots span.active{background:var(--blue)}

/* services */
.services{position:absolute;left:0;top:703px;width:1200px;height:308px;display:flex}
.service{width:400px;height:308px;color:var(--white);text-align:center;padding-top:52px}
.service-hunting{background:linear-gradient(180deg,#ff2ad6 0%,#e500b3 100%)}
.service-fishing{background:linear-gradient(180deg,#52bde6 0%,#1f6dc2 100%)}
.service-sports{background:linear-gradient(180deg,#7b48a8 0%,#3a1762 100%)}
.service svg{width:80px;height:80px}
.service h3{margin-top:24px;font-size:26px;font-weight:700;letter-spacing:.5px}
.service p{margin:16px auto 0;width:250px;font-size:12px;line-height:19px}

/* section titles */
.section-title{position:absolute;left:0;width:1200px;text-align:center;font-family:'Kaushan Script',cursive;font-weight:400;font-size:56px;line-height:70px;letter-spacing:-1px;background:linear-gradient(90deg,var(--blue) 38%,var(--purple) 50%,var(--ink) 62%);-webkit-background-clip:text;background-clip:text;color:transparent}
.videos-title{top:1096px}
.gallery-title{top:2244px}

/* media */
.media{position:absolute;overflow:hidden}
.video-one{left:144px;top:1215px;width:444px;height:281px;background:linear-gradient(135deg,#b494c9 0%,#6d5b6a 55%,#9a9a9a 100%)}
.video-two{left:612px;top:1215px;width:444px;height:281px;background:linear-gradient(160deg,#4b4b4b 0%,#c9cac8 50%,#7ab9b0 100%)}
.video-feature{left:22px;top:1671px;width:1156px;height:481px;background:linear-gradient(120deg,#5f6a5a 0%,#2f4a6a 30%,#8c7a6a 55%,#3f5f7f 80%,#6a5a4a 100%)}
.play{position:absolute;left:50%;top:50%;width:56px;height:56px;margin:-28px 0 0 -28px;border-radius:50%;background:var(--play)}
.play::after{content:"";position:absolute;left:21px;top:16px;border-left:20px solid var(--white);border-top:12px solid transparent;border-bottom:12px solid transparent}
.btn-more{position:absolute;left:490px;width:220px;height:57px;border-radius:29px;background:var(--button);color:var(--white);font-weight:700;font-size:15px;display:flex;align-items:center;justify-content:center}
.more-videos{top:1551px}
.more-gallery{top:3213px}

.gallery-item{width:295px;height:394px}
.g1{left:144px;top:2361px;background:linear-gradient(150deg,#8a7f74 0%,#d6c9b8 50%,#5f5a55 100%)}
.g2{left:453px;top:2361px;background:linear-gradient(180deg,#2b2b2b 0%,#7f3fb0 30%,#2a8fd0 55%,#f0b020 80%,#e05020 100%)}
.g3{left:761px;top:2361px;background:linear-gradient(160deg,#4a4a6a 0%,#1c1c1c 45%,#b0704a 100%)}
.g4{left:144px;top:2768px;background:linear-gradient(140deg,#2f8fa5 0%,#c9a58a 50%,#8a8f96 100%)}
.g5{left:453px;top:2768px;background:linear-gradient(170deg,#f2efe8 0%,#7a4a9a 55%,#3a2a5a 100%)}
.g6{left:761px;top:2768px;background:linear-gradient(170deg,#1c1c1c 0%,#d8d4cc 40%,#4a3020 100%)}

/* footer */
.footer{position:absolute;left:0;top:3316px;width:1200px;height:404px}
.footer-water{position:absolute;left:0;top:0;width:1200px;height:404px}
.footer-brand{position:absolute;left:0;top:110px;width:1200px;text-align:center;font-weight:700;font-size:34px;color:var(--pink);line-height:1.15}
.footer-copy{position:absolute;left:0;top:279px;width:1200px;text-align:center;font-size:15px;color:var(--white)}
.social{position:absolute;left:528px;top:338px;display:flex;gap:27px}
.social span{width:29px;height:29px;border-radius:5px;background:var(--white)}
</style>
</head>
<body>
<div class="page">

  <header class="hero">
    <div class="hero-art" role="img" aria-label="Illustrated mermaid sitting on a rock by the water"></div>
    <div class="element-wheel" role="img" aria-label="Elements wheel with water, air, earth, fire and spirit"></div>
    <svg class="hero-water" viewBox="0 0 1200 123" preserveAspectRatio="none" aria-hidden="true">
      <defs><linearGradient id="seaTop" x1="0" y1="0" x2="0" y2="1"><stop offset="0" stop-color="#3a5fe0"/><stop offset="1" stop-color="#2440b8"/></linearGradient></defs>
      <path d="M0 30 C120 10 220 40 340 22 C460 6 560 36 680 20 C800 6 920 34 1040 18 C1120 8 1170 20 1200 16 L1200 123 L0 123 Z" fill="url(#seaTop)"/>
    </svg>
    <div class="brand">Wendell's Otter Cove</div>
    <nav class="nav">
      <span class="btn-pill btn-login">LOGIN</span>
      <span class="btn-pill btn-register">REGISTRATION</span>
      <span class="menu-icon"><span></span><span></span><span></span></span>
    </nav>
    <h1 class="hero-title">UIS NOST<br>RUM EXER</h1>
    <p class="hero-text">Nemouis nostrum exercitationem ullam corporis suscipitius modi tempor</p>
    <span class="btn-start">GET STARTED</span>
    <div class="slider-dots"><span></span><span class="active"></span><span></span><span></span></div>
  </header>

  <section class="services">
    <div class="service service-hunting">
      <svg viewBox="0 0 80 80" fill="none" stroke="#fff" stroke-width="3" stroke-linecap="round" stroke-linejoin="round" aria-hidden="true">
        <path d="M28 30 L40 36 L52 30 L52 46 L40 64 L28 46 Z"/>
        <path d="M28 30 C18 26 12 18 12 8 M18 22 L10 20 M22 26 L16 30"/>
        <path d="M52 30 C62 26 68 18 68 8 M62 22 L70 20 M58 26 L64 30"/>
      </svg>
      <h3>HUNTING</h3>
      <p>Lorem ipsum dolor sit amet, consectetur adipiscing elit, sed do eiusmod tempor incididunt dolore magna aliqua</p>
    </div>
    <div class="service service-fishing">
      <svg viewBox="0 0 80 80" fill="none" stroke="#fff" stroke-width="3" stroke-linecap="round" stroke-linejoin="round" aria-hidden="true">
        <path d="M10 52 L64 52 L58 62 L16 62 Z"/>
        <rect x="30" y="36" width="16" height="16"/>
        <circle cx="38" cy="26" r="5"/>
        <path d="M42 30 L70 8 L72 40"/>
        <path d="M8 70 q4 -4 8 0 t8 0 t8 0 t8 0 t8 0 t8 0 t8 0"/>
      </svg>
      <h3>FISHING</h3>
      <p>Lorem ipsum dolor sit amet, consectetur adipiscing elit, sed do eiusmod tempor incididunt dolore magna aliqua</p>
    </div>
    <div class="service service-sports">
      <svg viewBox="0 0 80 80" fill="none" stroke="#fff" stroke-width="3" stroke-linecap="round" stroke-linejoin="round" aria-hidden="true">
        <path d="M32 6 C20 22 20 58 32 74 C44 58 44 22 32 6 Z"/>
        <ellipse cx="32" cy="40" rx="5" ry="9"/>
        <rect x="52" y="6" width="10" height="18" rx="3"/>
        <path d="M57 24 L57 56"/>
        <rect x="52" y="56" width="10" height="18" rx="3"/>
      </svg>
      <h3>OUTDOOR SPORTS</h3>
      <p>Lorem ipsum dolor sit amet, consectetur adipiscing elit, sed do eiusmod tempor incididunt dolore magna aliqua</p>
    </div>
  </section>

  <h2 class="section-title videos-title">OUR VIDEOS</h2>
  <div class="media video-one" role="img" aria-label="Video thumbnail of a woman with pastel hair"><span class="play"></span></div>
  <div class="media video-two" role="img" aria-label="Video thumbnail of a drink with a teal sugared rim"><span class="play"></span></div>
  <span class="btn-more more-videos">VIEW MORE VIDEOS</span>
  <div class="media video-feature" role="img" aria-label="Feature video thumbnail: collage of marina and boating photos"><span class="play"></span></div>

  <h2 class="section-title gallery-title">OUR GALLERY</h2>
  <div class="media gallery-item g1" role="img" aria-label="Bundles of wrapped sage sticks"></div>
  <div class="media gallery-item g2" role="img" aria-label="Chakra banner hanging in the store"></div>
  <div class="media gallery-item g3" role="img" aria-label="Engraved chakra stone spheres"></div>
  <div class="media gallery-item g4" role="img" aria-label="Owner smiling at the fuel pump"></div>
  <div class="media gallery-item g5" role="img" aria-label="Bags of chakra reminder chips with a handwritten sign"></div>
  <div class="media gallery-item g6" role="img" aria-label="Owner holding a photo collage board"></div>
  <span class="btn-more more-gallery">VIEW MORE VIDEOS</span>

  <footer class="footer">
    <svg class="footer-water" viewBox="0 0 1200 404" preserveAspectRatio="none" aria-hidden="true">
      <defs><linearGradient id="seaFoot" x1="0" y1="0" x2="0" y2="1"><stop offset="0" stop-color="#3158de"/><stop offset="1" stop-color="#2b62d6"/></linearGradient></defs>
      <path d="M0 56 C150 40 260 64 400 30 C500 8 600 20 700 14 C820 6 900 34 1020 28 C1110 22 1160 36 1200 40 L1200 404 L0 404 Z" fill="url(#seaFoot)"/>
    </svg>
    <div class="footer-brand">Wendell's<br>Otter Cove</div>
    <p class="footer-copy">© 2021 WendellsOtterCove. All rights reserved.Privacy Terms of Use</p>
    <div class="social"><span aria-label="Social link"></span><span aria-label="Social link"></span><span aria-label="Social link"></span></div>
  </footer>

</div>
</body>
</html>
```